Banner Ad for Resume Services Website

The add is for this web site: www.BrightFolioDesk.com

The site offers 4 different services:

- Resume Writing (by a Certified Professional Resume Writer)
- Resume Posting (posts your resume to 85 job sites)
- Resume Distribution (sends your resume to hundreds of recruiters)
- Resume Online website (created an online resume with a domain name to your name)

Colors to be used are Blue, Yellow, etc... please check the website for inspiration.

Check the web site to learn more.

Target Market(s)

Unemployed, Professionals who want to switch jobs, etc..

Industry/Entity Type

Learn

Requirements
Must have
• We definitely one this to be included on the banner:

"Free Resume Samples"

in order to attract clicks.
Nice to have
• Some of the words we suggest to include on the banner are:

"How Good is Your Resume? Ask a Professional !"

Should not have
• No animation !

Do not place the LOGO on the banner as our LOGO might change in the near future. If you already submitted a banner with the LOGO on it, you can replace it with any other graphic that has a Resume/Jobs/BusinessStaff related theme.

```html
<!DOCTYPE html>
<html lang="en">
<head>
<meta charset="utf-8">
<title>Free Resume Samples Banner</title>
<link rel="stylesheet" href="https://fonts.googleapis.com/css2?family=Nunito:wght@700;800;900&display=swap">
<style>
  :root {
    --blue-deep: #0b3f8f;
    --blue-mid: #1a6cc4;
    --blue-bright: #2c8be0;
    --blue-light: #9fd0f3;
    --blue-pale: #c9e6fa;
    --headline-tint: #cfe6fb;
    --navy-text: #0a3d8c;
    --orange-top: #ff9a2a;
    --orange-bottom: #e85a0a;
    --white: #ffffff;
  }
  html, body {
    margin: 0;
    padding: 0;
    width: 1200px;
    height: 148px;
    overflow: hidden;
    background: var(--white);
  }
  .banner {
    position: relative;
    width: 1200px;
    height: 148px;
    overflow: hidden;
    font-family: "Nunito", "Arial Rounded MT Bold", Arial, sans-serif;
  }
  .banner__backdrop {
    position: absolute;
    inset: 0;
    display: block;
  }
  .pitch {
    position: absolute;
    left: 46px;
    top: 22px;
    margin: 0;
  }
  .pitch__question {
    display: block;
    color: var(--headline-tint);
    font-weight: 800;
    font-size: 31px;
    line-height: 1;
    letter-spacing: 0.2px;
  }
  .pitch__answer {
    display: block;
    margin-top: 10px;
    color: var(--white);
    font-weight: 900;
    font-size: 53px;
    line-height: 1;
    letter-spacing: 0.3px;
    text-shadow: 0 2px 3px rgba(0, 20, 70, 0.35);
  }
  .offer {
    position: absolute;
    left: 791px;
    top: 14px;
    width: 376px;
    text-align: center;
  }
  .offer__title {
    margin: 0;
    color: var(--navy-text);
    font-weight: 900;
    font-size: 28px;
    line-height: 1;
    letter-spacing: 0.5px;
  }
  .offer__button {
    display: flex;
    align-items: center;
    justify-content: center;
    gap: 14px;
    margin-top: 18px;
    height: 63px;
    border-radius: 9px;
    background: linear-gradient(to bottom, var(--orange-top), var(--orange-bottom));
    box-shadow: 0 2px 4px rgba(0, 30, 80, 0.35), inset 0 1px 0 rgba(255, 255, 255, 0.45);
    color: var(--white);
    font-weight: 900;
    font-size: 35px;
    letter-spacing: 0.8px;
    text-decoration: none;
    text-shadow: 0 1px 2px rgba(120, 40, 0, 0.4);
  }
  .offer__arrow {
    width: 16px;
    height: 26px;
  }
</style>
</head>
<body>
  <div class="banner">
    <svg class="banner__backdrop" width="1200" height="148" viewBox="0 0 1200 148" aria-hidden="true">
      <defs>
        <linearGradient id="panel-light" x1="0" y1="0" x2="0" y2="1">
          <stop offset="0" stop-color="#b8def8"/>
          <stop offset="1" stop-color="#6fb4ea"/>
        </linearGradient>
        <linearGradient id="panel-mid" x1="0" y1="0" x2="1" y2="0">
          <stop offset="0" stop-color="#1f74cc"/>
          <stop offset="1" stop-color="#3b95e3"/>
        </linearGradient>
        <linearGradient id="panel-deep" x1="0" y1="0" x2="1" y2="0">
          <stop offset="0" stop-color="#0a3a88"/>
          <stop offset="0.6" stop-color="#0f4fa8"/>
          <stop offset="1" stop-color="#1962bf"/>
        </linearGradient>
      </defs>
      <rect class="panel-light" width="1200" height="148" fill="url(#panel-light)"/>
      <polygon class="panel-mid" points="0,0 660,0 712,74 660,148 0,148" fill="url(#panel-mid)"/>
      <polygon class="panel-deep" points="0,0 622,0 674,74 622,148 0,148" fill="url(#panel-deep)"/>
    </svg>

    <h1 class="pitch">
      <span class="pitch__question">How good is your resume?</span>
      <span class="pitch__answer">Ask a Professional.</span>
    </h1>

    <div class="offer">
      <p class="offer__title">FREE RESUME SAMPLES</p>
      <a class="offer__button" href="#">
        <span>CLICK HERE</span>
        <svg class="offer__arrow" viewBox="0 0 16 26" aria-hidden="true">
          <polyline points="3,3 13,13 3,23" fill="none" stroke="#ffffff" stroke-width="4.5" stroke-linecap="round" stroke-linejoin="round"/>
        </svg>
      </a>
    </div>
  </div>
</body>
</html>
```